Waistline Ember Product Social Media Graphics

Focusing on the Waistline Ember product, create 5-6 individual social media graphics (square size). For the color scheme of the graphics, they should all be complementary with the Waistline Ember bottle colors.
Note: each graphic should have one of the 2 pictures of the bottle on it and/or one of the images with a person on it (several pics attached)/only use stock photography that I provided.
Target Market(s)
For men and women trying to lose belly fat
Industry/Entity Type
health and wellness
Look and feel
Each slider illustrates characteristics of the customer's brand and the style your logo design should communicate.

```html
<!DOCTYPE html>
<html lang="en">
<head>
<meta charset="utf-8">
<title>Waistline Ember Social Graphics</title>
<link href="https://fonts.googleapis.com/css2?family=Poppins:wght@400;500;700;800&display=swap" rel="stylesheet">
<style>
:root{
  --red:#e8392b;
  --red-soft:#f4695a;
  --red-deep:#d92b1f;
  --white:#ffffff;
  --ink:#1d1d1d;
  --page:#ffffff;
  --bottle-hi:#ffffff;
  --bottle-lo:#d9dadc;
}
*{margin:0;padding:0;box-sizing:border-box}
html,body{width:1200px;height:1188px;overflow:hidden;background:var(--page)}
body{position:relative;font-family:'Poppins',sans-serif}
.tile{position:absolute;width:310px;height:310px;overflow:hidden;box-shadow:0 2px 8px rgba(0,0,0,.12)}
.photo{position:absolute;z-index:0}
.tile svg.bg{position:absolute;inset:0;width:310px;height:310px;z-index:1}
.bottle{position:absolute;z-index:2;border-radius:10px 10px 8px 8px;
  background:linear-gradient(90deg,var(--bottle-lo) 0%,var(--bottle-hi) 35%,var(--bottle-hi) 60%,var(--bottle-lo) 100%);
  box-shadow:0 6px 10px rgba(0,0,0,.18)}
.bottle::before{content:"";position:absolute;left:14%;right:14%;top:-14%;height:16%;border-radius:4px 4px 0 0;
  background:linear-gradient(90deg,#d5d6d8,#fff 40%,#e4e4e6)}
.bottle .name{position:absolute;left:0;right:0;top:42%;text-align:center;font-weight:700;color:var(--red);line-height:1}
.headline{position:absolute;z-index:3;font-weight:800;line-height:.98;letter-spacing:-.3px;white-space:nowrap}
.sub{position:absolute;z-index:3;font-weight:400;line-height:1.15;white-space:nowrap}
.white{color:var(--white)}
.red{color:var(--red)}
.ink{color:var(--ink)}
.right{text-align:right}
.pill{position:absolute;z-index:4;border-radius:20px;font-weight:700;white-space:nowrap;line-height:1}
.pill.solid{background:var(--red);color:var(--white)}
.pill.outline{border:1.5px solid var(--white);color:var(--white)}
</style>
</head>
<body>

<!-- Tile: belly bloat -->
<section class="tile" style="left:106px;top:89px;background:var(--red)">
  <div class="photo" role="img" aria-label="Slim woman in a white sports top holding out oversized jeans" style="left:196px;top:0;width:114px;height:310px;background:linear-gradient(180deg,#f2f2f4 0%,#a7714f 35%,#8d5a3d 60%,#7c9fc6 80%,#6f93bd 100%)"></div>
  <svg class="bg" viewBox="0 0 310 310"><path d="M0 210 C80 205 170 250 230 310 L0 310Z" fill="var(--white)"/><circle cx="210" cy="0" r="46" fill="none" stroke="var(--white)" stroke-opacity=".6"/></svg>
  <h2 class="headline white" style="left:16px;top:26px;font-size:27px">Belly Bloat<br>No More:</h2>
  <p class="sub white" style="left:16px;top:86px;font-size:12.5px">Discover the Secret<br>to a Flatter Tummy!</p>
  <div class="bottle" role="img" aria-label="Supplement bottle" style="left:24px;top:148px;width:80px;height:142px"><span class="name" style="font-size:11px">Waistline<br>Ember</span></div>
</section>

<!-- Tile: reduce belly fat fast -->
<section class="tile" style="left:444px;top:89px;background:var(--red)">
  <div class="photo" role="img" aria-label="Hands forming a heart shape over a bare stomach" style="left:0;top:0;width:310px;height:310px;background:linear-gradient(120deg,#caa184 0%,#9a6a4c 40%,#c9c9c9 75%)"></div>
  <svg class="bg" viewBox="0 0 310 310"><path d="M95 0 L310 0 L310 310 L150 310 C180 220 130 130 95 0Z" fill="var(--red)"/><path d="M160 310 C220 290 270 270 310 230 L310 310Z" fill="var(--white)"/></svg>
  <h2 class="headline white right" style="right:16px;top:22px;font-size:27px">Reduce Belly<br>Fat Fast:</h2>
  <p class="sub white right" style="right:16px;top:86px;font-size:12.5px">The Gut Cleanse<br>You Need to Try!</p>
  <div class="bottle" role="img" aria-label="Supplement bottle" style="left:148px;top:178px;width:62px;height:112px"><span class="name" style="font-size:8px">Waistline<br>Ember</span></div>
  <div class="bottle" role="img" aria-label="Supplement bottle" style="left:232px;top:178px;width:62px;height:112px"><span class="name" style="font-size:8px">Waistline<br>Ember</span></div>
  <div class="bottle" role="img" aria-label="Supplement bottle" style="left:188px;top:172px;width:66px;height:124px"><span class="name" style="font-size:9px">Waistline<br>Ember</span></div>
</section>

<!-- Tile: overnight, energy -->
<section class="tile" style="left:783px;top:89px;background:var(--white)">
  <div class="photo" role="img" aria-label="Smiling woman in a blue T-shirt holding out oversized jeans" style="left:0;top:0;width:132px;height:310px;background:linear-gradient(180deg,#f3f3f3 0%,#e9e4e0 30%,#4b78c0 50%,#6c8fb8 75%,#5a7fa8 100%)"></div>
  <svg class="bg" viewBox="0 0 310 310"><path d="M150 310 C200 280 230 200 310 160 L310 310Z" fill="var(--red)"/></svg>
  <h2 class="headline red right" style="right:8px;top:8px;font-size:23px;line-height:.97">Reduce<br>Belly Fat<br>and Bloating<br>Overnight!</h2>
  <span class="pill solid" style="left:122px;top:134px;padding:6px 10px;font-size:10px;transform:rotate(4deg)">Increased energy</span>
  <div class="bottle" role="img" aria-label="Supplement bottle" style="left:222px;top:152px;width:80px;height:140px"><span class="name" style="font-size:11px">Waistline<br>Ember</span></div>
</section>

<!-- Tile: flatter stomach, pink -->
<section class="tile" style="left:106px;top:439px;background:linear-gradient(120deg,#fbf7f6,#f7dfe0)">
  <div class="photo" role="img" aria-label="Woman in pink knitwear touching her waist" style="left:180px;top:0;width:130px;height:230px;background:linear-gradient(160deg,#f1b3bd,#e79aa8 60%,#f4d7d9)"></div>
  <svg class="bg" viewBox="0 0 310 310"><path d="M0 190 C90 210 200 240 310 200 L310 310 L0 310Z" fill="var(--red)"/></svg>
  <h2 class="headline red" style="left:17px;top:16px;font-size:25px">Want a<br>Flatter<br>Stomach?</h2>
  <p class="sub ink" style="left:17px;top:96px;font-size:12px">This Gut Cleanse<br>Could Be the Key!</p>
  <div class="bottle" role="img" aria-label="Supplement bottle" style="left:16px;top:160px;width:72px;height:132px"><span class="name" style="font-size:9px">Waistline<br>Ember</span></div>
  <div class="bottle" role="img" aria-label="Supplement bottle" style="left:126px;top:160px;width:72px;height:132px"><span class="name" style="font-size:9px">Waistline<br>Ember</span></div>
  <div class="bottle" role="img" aria-label="Supplement bottle" style="left:66px;top:154px;width:80px;height:144px"><span class="name" style="font-size:10px">Waistline<br>Ember</span></div>
</section>

<!-- Tile: toxins -->
<section class="tile" style="left:444px;top:439px;background:var(--red)">
  <div class="photo" role="img" aria-label="Woman measuring her slim waist with a tape measure" style="left:0;top:0;width:150px;height:310px;background:linear-gradient(180deg,#f4f4f4 0%,#c99a7a 30%,#b5835f 55%,#f2f2f2 78%,#d7a786 100%)"></div>
  <svg class="bg" viewBox="0 0 310 310"><path d="M70 310 C140 250 230 220 310 210 L310 310Z" fill="var(--white)"/><path d="M120 0 L310 0 L310 210 C230 210 170 200 150 120 C140 80 130 40 120 0Z" fill="var(--red)"/></svg>
  <h2 class="headline white right" style="right:13px;top:16px;font-size:29px">Get Rid<br>of Toxins</h2>
  <p class="sub white right" style="right:13px;top:82px;font-size:12.5px">to Reveal a<br>Flatter Tummy!</p>
  <span class="pill outline" style="left:100px;top:196px;padding:5px 8px;font-size:9px">Reduced bloating</span>
  <div class="bottle" role="img" aria-label="Supplement bottle" style="left:198px;top:148px;width:86px;height:150px"><span class="name" style="font-size:11px">Waistline<br>Ember</span></div>
</section>

<!-- Tile: digestion -->
<section class="tile" style="left:783px;top:439px;background:var(--white)">
  <div class="photo" role="img" aria-label="Smiling woman in a red sports top holding out oversized jeans" style="left:188px;top:0;width:122px;height:280px;background:linear-gradient(180deg,#f2f2f2 0%,#8a5a3f 30%,#ef3f5c 45%,#9a6445 65%,#6f93bd 85%)"></div>
  <svg class="bg" viewBox="0 0 310 310"><path d="M0 200 C100 230 200 280 310 250 L310 310 L0 310Z" fill="var(--red)"/></svg>
  <h2 class="headline red" style="left:8px;top:14px;font-size:31px;line-height:1">Reduce<br>Belly Fat</h2>
  <p class="sub ink" style="left:9px;top:92px;font-size:11px">and Bloating Overnight!</p>
  <span class="pill solid" style="left:30px;top:132px;padding:6px 10px;font-size:10px;transform:rotate(3deg)">Improved digestion</span>
  <div class="bottle" role="img" aria-label="Supplement bottle" style="left:8px;top:180px;width:66px;height:120px"><span class="name" style="font-size:8.5px">Waistline<br>Ember</span></div>
  <div class="bottle" role="img" aria-label="Supplement bottle" style="left:106px;top:180px;width:66px;height:120px"><span class="name" style="font-size:8.5px">Waistline<br>Ember</span></div>
  <div class="bottle" role="img" aria-label="Supplement bottle" style="left:52px;top:176px;width:72px;height:128px"><span class="name" style="font-size:9.5px">Waistline<br>Ember</span></div>
</section>

<!-- Tile: flatter stomach, red -->
<section class="tile" style="left:444px;top:788px;background:var(--red)">
  <div class="photo" role="img" aria-label="Slim woman in white sportswear with hand on hip" style="left:185px;top:0;width:125px;height:310px;background:linear-gradient(180deg,#f5f5f5 0%,#f0f0f0 25%,#b07a55 45%,#9c6a48 65%,#f2f2f2 80%,#a8764f 100%)"></div>
  <svg class="bg" viewBox="0 0 310 310"><path d="M0 210 C70 200 140 250 180 310 L0 310Z" fill="var(--white)"/><circle cx="150" cy="200" r="95" fill="none" stroke="var(--white)" stroke-opacity=".5"/></svg>
  <h2 class="headline white" style="left:16px;top:14px;font-size:26px;line-height:.88">Want a<br>Flatter<br>Stomach?</h2>
  <p class="sub white" style="left:16px;top:90px;font-size:8.5px">This Gut Cleanse Could Be the Key!</p>
  <div class="bottle" role="img" aria-label="Supplement bottle" style="left:26px;top:132px;width:92px;height:166px"><span class="name" style="font-size:12px">Waistline<br>Ember</span></div>
</section>

</body>
</html>
```